Design graphics and Print for a line of Herb Seeds- Envelope Design

We need a set of herb seed envelopes designed for a new seed line we are launching.
The design will be both front and back

Envelope will be a colored ( green) ) envelope with white text
or a white or cream envelope in all black /and images text. Or can add some colors to the white envelope.

I have attached the die-cut of the seed envelope.
I have attached some images of envelopes I like. Please do not copy, these are just to give you an idea of what I like.

Please feel free to reach out to me if you have any questions.

Thank you

Target Market(s)

The design needs to classic that can translate to 3 different audiences. 1. young parents 2. hip, young single millennial 3. kids

Industry/Entity Type

Ecommerce

Font styles to use
Serif

Requirements
Must have
• Please use the herb - Parsley for the design
Icon, Text or both.

Front side must have:
1.either herb Icon or work Parsley or both- this will be the main attraction
2. company name- Tall Meadow Pantry
3. can use design elements
4. can use my logo on from or back or not at all. I

Backside must have:
1. social media tags
FB, Snapgram and Pinboard ( use icons) @tallmeadowpantry

my website: www.tallmeadowpantry.example
this can be on from or back of the envelope.
Should not have
• please stay away from "county" flowery, old fashioned style designs

```html
<!DOCTYPE html>
<html lang="en">
<head>
<meta charset="utf-8">
<title>Tall Meadow Pantry – Parsley Seed Envelope</title>
<link href="https://fonts.googleapis.com/css2?family=Playfair+Display:wght@700&family=Montserrat:wght@300;400&display=swap" rel="stylesheet">
<style>
  :root {
    --forest: #19432f;
    --forest-text: #163d2a;
    --leaf: #2f6b45;
    --paper: #ffffff;
    --rule: #4a4a4a;
    --sprig-faint: #e3e9e6;
    --sprig-dark: #2c5a43;
    --sprig-white: #f6f7f6;
  }
  * { margin: 0; padding: 0; box-sizing: border-box; }
  html, body { width: 1200px; height: 1000px; overflow: hidden; background: var(--paper); }
  .canvas { position: relative; width: 1200px; height: 1000px; }

  /* Back panel */
  .back-panel {
    position: absolute; left: 100px; top: 182px; width: 488px; height: 701px;
    border: 1px solid var(--rule); background: var(--paper);
  }
  .brand-title {
    position: absolute; left: 0; width: 100%; text-align: center;
    font-family: "Playfair Display", Georgia, serif; font-weight: 700;
  }
  .back-panel .brand-title { top: 44px; font-size: 30px; color: var(--forest-text); }
  .tagline {
    position: absolute; top: 84px; width: 100%; text-align: center;
    font-family: "Montserrat", Arial, sans-serif; font-weight: 300; font-size: 20px; color: var(--leaf);
  }
  .sprig { position: absolute; border-radius: 46% 54% 40% 60%; }
  .sprig--back-top { left: 360px; top: 4px; width: 118px; height: 140px; background: var(--sprig-faint); opacity: .7; }
  .sprig--back-bottom { left: 8px; top: 462px; width: 180px; height: 184px; background: var(--sprig-faint); opacity: .7; }

  .brand-mark {
    position: absolute; left: 170px; top: 508px; display: flex; align-items: center; gap: 8px;
    font-family: "Playfair Display", Georgia, serif; font-weight: 700; font-size: 16px; color: var(--forest-text);
  }
  .brand-mark .dot { width: 22px; height: 22px; border-radius: 50%; background: var(--forest); }

  .socials {
    position: absolute; left: 102px; top: 584px; display: grid;
    grid-template-columns: 146px 140px; row-gap: 3px;
    font-family: "Montserrat", Arial, sans-serif; font-size: 19px; color: var(--forest-text);
  }
  .social { display: flex; align-items: center; gap: 14px; line-height: 21px; }
  .social .icon { width: 18px; height: 18px; border-radius: 50%; background: var(--forest); flex: none; }
  .web-back {
    position: absolute; top: 640px; width: 100%; text-align: center;
    font-family: "Montserrat", Arial, sans-serif; font-size: 22px; color: var(--forest-text);
  }

  /* Front panel */
  .front-panel { position: absolute; left: 588px; top: 119px; width: 508px; height: 764px; }
  .front-panel svg.envelope { position: absolute; left: 0; top: 0; }
  .sprig--front-left { left: 32px; top: 66px; width: 74px; height: 60px; background: var(--sprig-dark); opacity: .6; }
  .sprig--front-right { left: 396px; top: 100px; width: 112px; height: 170px; background: var(--sprig-dark); opacity: .6; }
  .front-mark { position: absolute; left: 243px; top: 87px; width: 32px; height: 32px; border-radius: 50%; background: var(--paper); }
  .front-panel .brand-title { top: 122px; font-size: 21px; color: var(--paper); }
  .herb-label {
    position: absolute; left: 126px; top: 180px; width: 264px; height: 69px; border-radius: 20px;
    background: var(--paper); display: flex; align-items: center; justify-content: center;
    font-family: "Playfair Display", Georgia, serif; font-weight: 700; font-size: 35px; color: var(--forest-text);
  }
  .hero-herb {
    position: absolute; left: 84px; top: 290px; width: 322px; height: 388px;
    background: radial-gradient(ellipse at 50% 45%, var(--sprig-white) 0%, rgba(246,247,246,.85) 55%, rgba(246,247,246,0) 72%);
  }
  .web-front {
    position: absolute; top: 726px; width: 100%; text-align: center;
    font-family: "Montserrat", Arial, sans-serif; font-size: 16px; color: var(--paper);
  }
</style>
</head>
<body>
<div class="canvas">

  <section class="back-panel">
    <div class="sprig sprig--back-top" role="img" aria-label="Faint line drawing of a parsley sprig"></div>
    <h1 class="brand-title">Tall Meadow Pantry</h1>
    <p class="tagline">Grow your Own!</p>
    <div class="sprig sprig--back-bottom" role="img" aria-label="Faint line drawing of a parsley branch"></div>
    <div class="brand-mark"><span class="dot"></span>Tall Meadow Pantry</div>
    <ul class="socials">
      <li class="social"><span class="icon"></span>Pinboard</li>
      <li class="social"><span class="icon"></span>Snapgram</li>
      <li class="social"><span class="icon"></span>Tubecast</li>
      <li class="social"><span class="icon"></span>Friendbook</li>
    </ul>
    <p class="web-back">www.tallmeadowpantry.example</p>
  </section>

  <section class="front-panel">
    <svg class="envelope" width="508" height="764" viewBox="0 0 508 764" aria-hidden="true">
      <path d="M0 44 A44 44 0 0 1 44 0 H464 A44 44 0 0 1 508 44 V764 H0 Z" fill="var(--forest)"/>
      <line x1="0" y1="64.5" x2="508" y2="64.5" stroke="#0f2e20" stroke-width="1"/>
    </svg>
    <div class="sprig sprig--front-left" role="img" aria-label="Subtle parsley leaf decoration"></div>
    <div class="sprig sprig--front-right" role="img" aria-label="Subtle parsley sprig decoration"></div>
    <div class="front-mark"></div>
    <h2 class="brand-title">Tall Meadow Pantry</h2>
    <div class="herb-label">PARSELY</div>
    <div class="hero-herb" role="img" aria-label="Large white silhouette illustration of a flat-leaf parsley sprig"></div>
    <p class="web-front">www.tallmeadowpantry.example</p>
  </section>

</div>
</body>
</html>
```